Velio shoes is a wholesale shoe sales company , mostly working in female shoes and kiddies shoes with a small mens section . looking for a clean slick look. http://www.brindafeet.co.za/shop/ is a good reference

It Company

```html
<!DOCTYPE html>
<html lang="en">
<head>
<meta charset="utf-8">
<title>Velio shoes</title>
<link href="https://fonts.googleapis.com/css2?family=Open+Sans:wght@400;600&display=swap" rel="stylesheet">
<style>
:root{
  --blue:#1aa3cf;
  --ink:#2b2b2b;
  --muted:#666;
  --soft:#999;
  --line:#dcdcdc;
  --band:#f2f2f3;
  --foot:#c9c9cd;
  --violet:#7d6b98;
  --black:#111;
}
*{box-sizing:border-box;margin:0;padding:0}
html,body{width:810px;height:1200px;overflow:hidden;background:#fff}
body{font-family:"Open Sans",sans-serif;color:var(--ink);position:relative}
.abs{position:absolute}
a{color:inherit;text-decoration:none}

.brand{left:138px;top:28px;font-size:34px;font-weight:400;color:var(--black);letter-spacing:-1px;line-height:40px}
.account{left:508px;top:13px;font-size:11px;color:var(--ink);display:flex;align-items:center;gap:4px}
.account .sep{width:1px;height:15px;background:var(--ink)}
.search{left:600px;top:13px;width:72px;height:14px;border:1px solid var(--violet);font-size:7px;font-style:italic;color:var(--soft);padding:1px 0 0 9px}
.search svg{position:absolute;right:6px;top:2px}
.call{left:511px;top:45px;display:flex;align-items:center;gap:13px;color:var(--blue);font-size:12px}
.call b{font-weight:400;color:var(--violet)}

.nav{left:138px;top:87px;width:534px;height:20px;border:1px solid var(--line);display:flex;font-size:8px;align-items:center}
.nav a{margin-left:4px;margin-right:24px;color:var(--ink)}
.nav a.active{color:var(--blue);border-bottom:1px solid var(--blue)}

.hero{left:138px;top:111px;width:534px;height:217px;background:linear-gradient(90deg,#8a5a3c 0%,#c79a7c 22%,#5a4a44 38%,#e0c040 48%,#eeeef0 62%,#e6e6ea 100%)}
.hero-shadow{left:138px;top:328px;width:534px;height:22px;background:radial-gradient(ellipse at top,rgba(0,0,0,.12),transparent 70%)}
.hero-copy{left:440px;top:150px;width:185px;text-align:right}
.hero-copy h2{font-size:14px;font-weight:400;color:var(--violet);margin-bottom:10px}
.hero-copy p{font-size:8px;line-height:14px;color:#444}
.shop-now{left:508px;top:255px;width:104px;height:29px;background:var(--blue);color:#fff;font-size:13px;display:flex;align-items:center;justify-content:center}
.hero-arrow{width:20px;height:20px;border-radius:50%;background:rgba(150,150,150,.45)}
.dots{left:390px;top:312px;display:flex;gap:2px}
.dots i{width:5px;height:5px;border-radius:50%;background:#aaa}
.dots i.on{background:var(--blue)}

.tab{height:29px;background:var(--blue);color:#fff;font-size:13.5px;display:flex;align-items:center;padding-left:8px}
.arrivals{left:138px;top:379px;width:118px}
.cats{left:578px;top:379px;width:93px}
.next{left:451px;top:386px}
.cat-list{left:581px;top:420px;list-style:none;font-size:10px;color:var(--muted)}
.cat-list li{height:26px;display:flex;align-items:center;gap:6px}
.cat-list li::before{content:"";border-left:3px solid var(--muted);border-top:2px solid transparent;border-bottom:2px solid transparent}

.product{width:100px;height:93px;border:1px solid var(--blue);background:#fff}
.product .thumb{margin:6px 8px;height:58px}
.product .bar{position:absolute;left:-1px;right:-1px;bottom:-1px;height:22px;display:flex}
.product .name{flex:1;background:var(--black);color:#fff;font-size:8.5px;display:flex;align-items:center;padding-left:8px}
.product .cart{width:26px;background:var(--blue);display:flex;align-items:center;justify-content:center}
.t-blue{background:linear-gradient(135deg,#2a3a8a,#d45aa0 50%,#2fb8a8)}
.t-orange{background:linear-gradient(135deg,#f6e0c8,#e07a2a 45%,#fff 80%)}
.t-red{background:linear-gradient(135deg,#b81620,#e0303a 50%,#7a0f14)}

.more-head{left:137px;top:756px;width:535px;height:26px;border-bottom:2px solid var(--line);display:flex;justify-content:space-between;font-size:13.5px;color:var(--blue)}
.more-shoe{top:812px;height:64px;width:78px}
.chev{top:830px}

.band{left:0;top:920px;width:810px;height:64px;background:var(--band)}
.signup{left:147px;top:938px;font-size:14px;line-height:20px;color:var(--blue)}
.email{left:446px;top:942px;width:216px;height:27px;border:2px solid var(--blue);background:#fff;display:flex}
.email .field{flex:1;font-size:8.5px;font-style:italic;color:var(--blue);padding:6px 0 0 20px}
.email .go{width:34px;flex:none;border-left:2px solid var(--blue);display:flex;align-items:center;justify-content:center}

.foot-h{top:1022px;font-size:13.5px;font-weight:400;color:var(--ink)}
.about{left:197px;top:1055px;width:136px;font-size:7.5px;line-height:12px;color:var(--muted)}
.links{left:390px;top:1056px;list-style:none;font-size:7.5px;line-height:13.8px;color:var(--soft)}
.contact{left:508px;top:1053px;list-style:none;font-size:7.5px;color:var(--muted)}
.contact li{height:18px;display:flex;align-items:center;gap:9px}
.contact li .ic{width:10px;display:flex;justify-content:center}

.bottom{left:0;top:1170px;width:810px;height:30px;background:var(--foot)}
.copy{left:138px;top:1179px;font-size:8.5px;color:#444}
.social{left:604px;top:1180px;display:flex;gap:7px}
.social i{display:block;width:11px;height:11px;border-radius:50%;background:var(--blue)}
</style>
</head>
<body>

<header>
  <div class="abs brand">Velio shoes</div>
  <div class="abs account"><a href="#">Log in</a><span class="sep"></span><a href="#">Register</a></div>
  <div class="abs search">Search
    <svg width="9" height="9" viewBox="0 0 9 9"><circle cx="3.5" cy="3.5" r="2.6" fill="none" stroke="#888" stroke-width="1"/><line x1="5.5" y1="5.5" x2="8.5" y2="8.5" stroke="#888" stroke-width="1.2"/></svg>
  </div>
  <div class="abs call">
    <svg width="27" height="27" viewBox="0 0 27 27"><circle cx="13.5" cy="13.5" r="12.3" fill="none" stroke="#1aa3cf" stroke-width="1.6"/><path d="M9 7.5c1-.6 1.8 0 2.4 1.4l.6 1.5c.3.8-.4 1.4-1 1.9.7 1.7 2 3 3.7 3.9.5-.6 1.1-1.3 1.9-1l1.5.6c1.4.6 2 1.4 1.4 2.4-.8 1.3-2.4 2-4 1.4-3.6-1.4-6.2-4.1-7.6-7.7-.6-1.6.1-3.2 1.1-3.4z" fill="#1aa3cf"/></svg>
    <span>Call Us <b>012-555-0142</b></span>
  </div>
  <nav class="abs nav">
    <a class="active" href="#">HOME</a><a href="#">LADIES</a><a href="#">MENS</a><a href="#">KIDS</a><a href="#">Gallery</a><a href="#">Contact US</a>
  </nav>
</header>

<section class="hero-section">
  <div class="abs hero" role="img" aria-label="Smiling woman holding up several pairs of women's shoes and a handbag"></div>
  <div class="abs hero-shadow"></div>
  <div class="abs hero-arrow" style="left:157px;top:211px"></div>
  <div class="abs hero-arrow" style="left:631px;top:211px;background:rgba(120,120,120,.35)"></div>
  <div class="abs hero-copy">
    <h2>Pellentesque accumsan</h2>
    <p>Lorem ipsum is a dummy text only.<br>Dolor sit amet, consectetur<br>adipiscing elit. Nullam felis mauris,<br>eleifend ac rhoncus non,</p>
  </div>
  <a class="abs shop-now" href="#">Shop Now</a>
  <div class="abs dots"><i></i><i class="on"></i><i></i><i></i></div>
</section>

<section class="arrivals-section">
  <div class="abs tab arrivals">Latest Arrivals</div>
  <svg class="abs next" width="14" height="14" viewBox="0 0 14 14"><circle cx="7" cy="7" r="7" fill="#9a9a9a"/><path d="M4 7h5M7 4.5 9.5 7 7 9.5" stroke="#fff" stroke-width="1.6" fill="none"/></svg>

  <div class="abs product" style="left:138px;top:452px"><div class="thumb t-blue" role="img" aria-label="Blue high-heel sandals"></div><div class="bar"><span class="name">Lorem Ipsum</span><span class="cart"><svg width="12" height="10" viewBox="0 0 12 10"><path d="M1 4h10l-1.5 5.5h-7z" fill="none" stroke="#fff" stroke-width="1.2"/><path d="M4 4 6.5 .8M8 4 6.5 .8" stroke="#fff"/></svg></span></div></div>
  <div class="abs product" style="left:254px;top:452px"><div class="thumb t-orange" role="img" aria-label="Orange pumps"></div><div class="bar"><span class="name">Lorem Ipsum</span><span class="cart"><svg width="12" height="10" viewBox="0 0 12 10"><path d="M1 4h10l-1.5 5.5h-7z" fill="none" stroke="#fff" stroke-width="1.2"/><path d="M4 4 6.5 .8M8 4 6.5 .8" stroke="#fff"/></svg></span></div></div>
  <div class="abs product" style="left:370px;top:452px"><div class="thumb t-red" role="img" aria-label="Red ankle boots"></div><div class="bar"><span class="name">Lorem Ipsum</span><span class="cart"><svg width="12" height="10" viewBox="0 0 12 10"><path d="M1 4h10l-1.5 5.5h-7z" fill="none" stroke="#fff" stroke-width="1.2"/><path d="M4 4 6.5 .8M8 4 6.5 .8" stroke="#fff"/></svg></span></div></div>
  <div class="abs product" style="left:138px;top:589px"><div class="thumb t-blue" role="img" aria-label="Blue high-heel sandals"></div><div class="bar"><span class="name">Lorem Ipsum</span><span class="cart"><svg width="12" height="10" viewBox="0 0 12 10"><path d="M1 4h10l-1.5 5.5h-7z" fill="none" stroke="#fff" stroke-width="1.2"/><path d="M4 4 6.5 .8M8 4 6.5 .8" stroke="#fff"/></svg></span></div></div>
  <div class="abs product" style="left:254px;top:589px"><div class="thumb t-orange" role="img" aria-label="Orange pumps"></div><div class="bar"><span class="name">Lorem Ipsum</span><span class="cart"><svg width="12" height="10" viewBox="0 0 12 10"><path d="M1 4h10l-1.5 5.5h-7z" fill="none" stroke="#fff" stroke-width="1.2"/><path d="M4 4 6.5 .8M8 4 6.5 .8" stroke="#fff"/></svg></span></div></div>
  <div class="abs product" style="left:370px;top:589px"><div class="thumb t-red" role="img" aria-label="Red ankle boots"></div><div class="bar"><span class="name">Lorem Ipsum</span><span class="cart"><svg width="12" height="10" viewBox="0 0 12 10"><path d="M1 4h10l-1.5 5.5h-7z" fill="none" stroke="#fff" stroke-width="1.2"/><path d="M4 4 6.5 .8M8 4 6.5 .8" stroke="#fff"/></svg></span></div></div>

  <div class="abs tab cats">Categories</div>
  <ul class="abs cat-list">
    <li>Pellentesque</li><li>Accumsan</li><li>Dignissim</li><li>Libero eu</li><li>Dignissim</li><li>Aliquam sed</li><li>Accumsan</li>
  </ul>
</section>

<section class="more-section">
  <div class="abs more-head"><span>Other Items You May Like</span><span>See All</span></div>
  <svg class="abs chev" style="left:137px" width="16" height="24" viewBox="0 0 16 24"><path d="M14 1 2 12l12 11" fill="none" stroke="#ccc" stroke-width="1.5"/></svg>
  <svg class="abs chev" style="left:656px" width="16" height="24" viewBox="0 0 16 24"><path d="M2 1l12 11L2 23" fill="none" stroke="#ccc" stroke-width="1.5"/></svg>
  <div class="abs more-shoe" style="left:165px;background:linear-gradient(135deg,#fff,#d01818 45%,#8a0c0c 75%,#fff)" role="img" aria-label="Red platform pumps"></div>
  <div class="abs more-shoe" style="left:264px;background:linear-gradient(135deg,#fff,#e58a3a 45%,#b85a20 70%,#fff)" role="img" aria-label="Orange pumps"></div>
  <div class="abs more-shoe" style="left:368px;background:linear-gradient(135deg,#fff,#b89078 45%,#8a6a58 75%,#fff)" role="img" aria-label="Taupe peep-toe heels"></div>
  <div class="abs more-shoe" style="left:472px;background:linear-gradient(135deg,#fff,#2a3a80 45%,#d8a878 75%,#fff)" role="img" aria-label="Navy heels"></div>
  <div class="abs more-shoe" style="left:562px;background:linear-gradient(135deg,#fff,#4a2a20 45%,#1a1210 70%,#fff)" role="img" aria-label="Dark brown heels"></div>
</section>

<section>
  <div class="abs band"></div>
  <p class="abs signup">Sign up to our newsletter and receive<br>discounts and special offers</p>
  <div class="abs email"><span class="field">Enter email address</span><span class="go"><svg width="16" height="16" viewBox="0 0 16 16"><circle cx="8" cy="8" r="8" fill="#1aa3cf"/><path d="M4 8h6M7.5 5 10.5 8 7.5 11" stroke="#fff" stroke-width="1.8" fill="none"/></svg></span></div>
</section>

<footer>
  <h3 class="abs foot-h" style="left:196px">About Velio shoes</h3>
  <p class="abs about">Lorem ipsum is a dummy text only. Dolor sit amet, consectetur adipiscing elit. Nullam felis mauris, eleifend ac rhoncus non, lobortis at diam.</p>
  <h3 class="abs foot-h" style="left:389px">Quick Links</h3>
  <ul class="abs links"><li>HOME</li><li>LADIES</li><li>MENS</li><li>KIDS</li><li>Gallery</li><li>Contact US</li></ul>
  <h3 class="abs foot-h" style="left:518px">Contact Us</h3>
  <ul class="abs contact">
    <li><span class="ic"><svg width="10" height="9" viewBox="0 0 10 9"><path d="M5 0 10 4.5H8.5V9h-2.3V6H3.8v3H1.5V4.5H0z" fill="#1aa3cf"/></svg></span>Store Manager</li>
    <li><span class="ic"></span>18 Elm Row St</li>
    <li><span class="ic"></span>Northfield, NF2 4QT</li>
    <li><span class="ic"><svg width="6" height="9" viewBox="0 0 6 9"><rect x=".6" y=".6" width="4.8" height="7.8" rx=".8" fill="none" stroke="#1aa3cf" stroke-width="1.2"/></svg></span>0845 000 1234</li>
    <li><span class="ic"><svg width="10" height="7" viewBox="0 0 10 7"><rect width="10" height="7" fill="#1aa3cf"/><path d="M0 0 5 4 10 0" stroke="#fff" fill="none"/></svg></span>hello@velioshoes.example</li>
  </ul>
  <div class="abs bottom"></div>
  <p class="abs copy">Copyright©Velio shoes. All Rights Reserved. 2014</p>
  <div class="abs social"><i></i><i></i><i></i><i></i></div>
</footer>

</body>
</html>
```